Zafiran - Echoes of a quiet road

🎨 Design Guidelines
1. Overall Impression

Dignified, spiritual, timeless

Central focus on sand dunes with footsteps as the main motif

Mood: calm, light, spirituality, hope

2. Color Scheme

Background: warm sand tones (beige, golden, brown)

Light source (sun/beam): soft gold/white

Typography: gold or warm yellow, metallic effect preferred (gold foil in print)

Spine and back cover: darker gradient from sand tones to deep blue/black for strong readability

3. Imagery

Front cover: sand dunes with clear footsteps leading towards light/horizon

No figurative depictions of people

Optional: subtle Islamic ornaments or geometric borders as a background accent

4. Typography

Title: “Ẓāfirān” → large, serif font, elegant, in gold

Subtitle: “Echoes of a Quiet Road” → smaller, clean & modern, also gold/white

Author: Hamid-Tariq Wasim an-Nūrī → bottom of the front cover, smaller size

Spine: Title + Arabic word زافيران vertically placed, harmonized with the style

5. Back Cover

Short blurb/description (provided by client)

Highlighted keywords in large type: "Courage. Integrity. Faith."

ISBN + barcode at the bottom left

Background: continuation of the sand texture from the front cover (with or without footsteps)

6. Finishing Options (Print)

Gold foil stamping for the title

Matte cover with selective gloss (eg on the light or ornaments)

High-quality, sturdy cover stock

Target Market(s)

Islamic

Font styles to use
Serif

Requirements
Must have
• read the guidelines!
Nice to have
• read the guidelines!
Should not have
• read the guidelines!

```html
<!DOCTYPE html>
<html lang="en">
<head>
<meta charset="utf-8">
<title>Zafiran - Echoes of a quiet road</title>
<link rel="stylesheet" href="https://fonts.googleapis.com/css2?family=Playfair+Display:wght@700;800&family=Cormorant+Garamond:wght@500;600&family=Amiri:wght@700&family=Roboto:wght@400&display=swap">
<style>
  :root {
    --page-bg: #efe6d6;
    --navy-deep: #14283a;
    --navy: #1c3a4f;
    --teal-haze: #5d7a78;
    --sun-glow: #f4e9b8;
    --sand-light: #d6a850;
    --sand: #b98331;
    --sand-dark: #7e5420;
    --gold-light: #fff2b8;
    --gold: #f1c24a;
    --gold-deep: #b9801c;
    --frame-line: rgba(225, 215, 190, 0.55);
    --author: #f3ead2;
  }
  * { margin: 0; padding: 0; box-sizing: border-box; }
  html, body {
    width: 1200px; height: 1200px; overflow: hidden;
    background: var(--page-bg);
  }
  .canvas {
    position: relative; width: 1200px; height: 1200px;
    display: flex; align-items: center; justify-content: center;
  }
  .front-cover {
    position: relative; width: 720px; height: 1080px; overflow: hidden;
    background: linear-gradient(180deg, var(--navy-deep) 0%, var(--navy) 30%, var(--teal-haze) 46%, var(--sand-light) 58%, var(--sand) 78%, var(--sand-dark) 100%);
  }
  .dune-scene {
    position: absolute; left: 0; right: 0; top: 460px; bottom: 0;
    background:
      radial-gradient(ellipse 45% 18% at 50% 14%, rgba(255, 248, 210, 0.85), rgba(255, 240, 190, 0) 100%),
      linear-gradient(180deg, rgba(214, 168, 80, 0) 0%, rgba(200, 150, 62, 0.6) 30%, rgba(160, 108, 40, 0.7) 100%);
  }
  .cover-frame {
    position: absolute; inset: 34px;
    border: 1.5px solid var(--frame-line);
    pointer-events: none;
  }
  .title-block {
    position: absolute; top: 118px; left: 0; right: 0; text-align: center;
  }
  .gold-text {
    background: linear-gradient(180deg, var(--gold-light) 0%, var(--gold) 45%, var(--gold-deep) 100%);
    -webkit-background-clip: text; background-clip: text; color: transparent;
  }
  .title {
    font-family: "Playfair Display", Georgia, serif;
    font-weight: 800; font-size: 118px; line-height: 1; letter-spacing: 1px;
  }
  .subtitle {
    margin-top: 14px;
    font-family: "Cormorant Garamond", "Times New Roman", serif;
    font-weight: 600; font-size: 44px; line-height: 1;
  }
  .arabic-title {
    position: absolute; top: 300px; left: 0; right: 0; text-align: center;
    font-family: "Amiri", serif; font-weight: 700; font-size: 120px; line-height: 1.3;
    direction: rtl;
  }
  .medallion {
    position: absolute; top: 500px; left: 50%; width: 106px; height: 106px;
    margin-left: -53px; border-radius: 50%;
    background: radial-gradient(circle at 40% 35%, var(--gold-light), var(--gold) 55%, var(--gold-deep));
    box-shadow: 0 0 40px rgba(255, 240, 190, 0.7);
  }
  .author {
    position: absolute; bottom: 110px; left: 0; right: 0; text-align: center;
    font-family: "Roboto", Arial, sans-serif; font-size: 33px; color: var(--author);
    letter-spacing: 0.3px;
  }
</style>
</head>
<body>
<main class="canvas">
  <section class="front-cover">
    <div class="dune-scene" role="img" aria-label="Golden sand dunes with a line of footsteps leading toward a glowing horizon"></div>
    <div class="cover-frame"></div>
    <header class="title-block">
      <h1 class="title gold-text">Ẓāfirān</h1>
      <p class="subtitle gold-text">Echoes of a Quiet Road</p>
    </header>
    <p class="arabic-title gold-text" lang="ar">زافيران</p>
    <div class="medallion" role="img" aria-label="Round gold calligraphic medallion"></div>
    <p class="author">Hamid-Tariq Wasim an-Nūrī</p>
  </section>
</main>
</body>
</html>
```